Korellas Einfühlungsvermögen in das Projekt, ihre Nachfragen an der richtigen Stelle und ihre frischen Ideen haben zu einem ebook-Cover geführt, mit dem ich sehr zufrieden bin. Die Kommunikation war sehr angenehm und professionell. Danke!
Zielgruppe
E-Book: Satirische Kurzgeschichten rund um Schule und Bildung.
Zielgruppe: Leute mit Humor und Interesse an einem Einblick ins Klassenzimmer einer jungen Berliner Lehrerin. Schüler, Eltern, Lehrer, Referendare...
Aufgabenstellung
Möglichst keine Comics mit Sprechblasen, eher stilvoll, intellektuell, trotzdem frisch, jung und modern.
Helle Farben, gerne Andeutungen der Themen Schule, Bildung, Unterricht.
Die Kurzgeschichten meines E-Books sind schnelle Momentaufnahmen, sie könnten auch als Blog erscheinen statt als Buch, evtl. lässt sich dies auch im Design widerspiegeln (?).

```html
<!DOCTYPE html>
<html lang="de">
<head>
<meta charset="utf-8">
<title>Kreide und Kaffee – Helga Prinz</title>
<link rel="stylesheet" href="https://fonts.googleapis.com/css2?family=Cormorant+Garamond:wght@500&family=Allura&family=Caveat+Brush&display=swap">
<style>
  :root {
    --page: #ffffff;
    --sky: #86d8f0;
    --sky-deep: #62c8ea;
    --dress: #c8283a;
    --dress-deep: #b01e31;
    --label: #ffffff;
    --author: #c21f45;
    --title: #f7f03c;
    --subtitle: #3cc3ea;
  }
  * { margin: 0; padding: 0; box-sizing: border-box; }
  html, body {
    width: 1200px;
    height: 800px;
    overflow: hidden;
    background: var(--page);
  }
  .stage {
    position: relative;
    width: 1200px;
    height: 800px;
  }
  .cover {
    position: absolute;
    left: 330px;
    top: 30px;
    width: 540px;
    height: 740px;
    overflow: hidden;
    background: var(--sky);
  }
  .cover-photo {
    position: absolute;
    inset: 0;
    background: linear-gradient(180deg,
      var(--sky) 0%,
      var(--sky-deep) 42%,
      var(--dress) 66%,
      var(--dress-deep) 100%);
  }
  .author-label {
    position: absolute;
    left: 26%;
    top: 11%;
    width: 60%;
    height: 13%;
    background: var(--label);
    display: flex;
    align-items: center;
    justify-content: center;
  }
  .author-name {
    font-family: "Cormorant Garamond", serif;
    font-weight: 500;
    font-size: 34px;
    letter-spacing: 1px;
    color: var(--author);
    text-transform: uppercase;
  }
  .title {
    position: absolute;
    left: 4%;
    top: 28%;
    width: 92%;
    text-align: center;
    font-family: "Allura", cursive;
    font-weight: 400;
    font-size: 120px;
    line-height: 1.15;
    color: var(--title);
  }
  .subtitle {
    position: absolute;
    left: 15%;
    top: 68%;
    width: 70%;
    text-align: center;
    font-family: "Caveat Brush", cursive;
    font-size: 62px;
    line-height: 1.5;
    color: var(--subtitle);
  }
</style>
</head>
<body>
  <main class="stage">
    <section class="cover">
      <div class="cover-photo" role="img" aria-label="Foto: junge Lehrerin im roten gepunkteten Kleid vor hellblauem Hintergrund, mit einem Bücherstapel auf der Hand"></div>
      <div class="author-label">
        <span class="author-name">Helga Prinz</span>
      </div>
      <h1 class="title">Kreide und<br>Kaffee.</h1>
      <p class="subtitle">Notizen vom<br>Lehrerpult</p>
    </section>
  </main>
</body>
</html>
```